Spa Business Card Design Project

Hello! We are a boutique spa for men and women that is rebranding. I would like a memorable new business card that showcases our beautiful new logo and our unique business. I would like it to be classic/timeless and eclectic/artistic at the  same time.
I am a fan of negative space as you can tell from the logo. I am also open to any creative ideas.
Multi sided design. Two sided design is acceptable as an option, too. "Flaps/folds/whatever the design term is" are optional- whether full vertical or horizontal, half flap, full flap etc
On either side next to the golden snail I would potentially like to see "slow down. Enjoy Life."  Possibly on one statment on top of each other, crowned with the snail. Or the statment following the snail on one line... I am open for a creative suprise, too.
The back I would like room for the standard Information
"3817 Birch Lane
Ashbrook, New York 12496
(607) 462 3085
info@thecorvella spa.com
The snail is to be done in gold ink.
Can I also Have an option for cards that are individualized for staff members, too?

Updates
Project Deadline Extended
Reason: I apologize for the deadline extension. My day was more involved than anticipated in other matters. Hope to have this closed by next Tuesday.
Thank you

Target Market(s)
Men and women with expendable income between the ages of 30-55
Industry/Entity Type
Boutique
Requirements
Must have
- only black and gold ink.

Nice to have
- One of a kind.
Showcase the snail :-)
make you smile :-)
Fun, but professional.
Should not have
- Lots of color.
Too feminine.
Too busy.

```html
<!DOCTYPE html>
<html lang="en">
<head>
<meta charset="utf-8">
<title>The Corvella Spa – Business Card</title>
<link rel="stylesheet" href="https://fonts.googleapis.com/css2?family=Cinzel:wght@500&family=Open+Sans:wght@400;600;700&display=swap">
<style>
  :root {
    --gold: #cfaa62;
    --ink: #111111;
    --paper: #ffffff;
    --backdrop: #efeae2;
    --shadow: rgba(60, 45, 20, 0.22);
  }
  * { box-sizing: border-box; margin: 0; padding: 0; }
  html, body { width: 1200px; height: 1000px; overflow: hidden; }
  body {
    background: var(--backdrop);
    font-family: "Open Sans", Arial, sans-serif;
    position: relative;
  }
  .card {
    position: absolute;
    top: 350px;
    width: 540px;
    height: 300px;
    border-radius: 16px;
    overflow: hidden;
    box-shadow: 0 6px 18px var(--shadow);
  }
  .card--front { left: 46px; background: var(--paper); }
  .card--back { left: 618px; background: var(--gold); }

  /* Front */
  .brand {
    position: absolute;
    top: 66px;
    left: 0;
    width: 100%;
    text-align: center;
    color: var(--ink);
  }
  .brand__name {
    font-family: "Cinzel", Georgia, serif;
    font-weight: 500;
    line-height: 1;
  }
  .brand__the { display: block; font-size: 26px; }
  .brand__main { display: block; font-size: 38px; letter-spacing: 1px; margin-top: 2px; }
  .brand__spa { display: block; font-size: 30px; margin-top: 2px; }
  .brand__tagline {
    margin-top: 6px;
    font-size: 11px;
    font-weight: 400;
  }
  .front__band {
    position: absolute;
    left: 0; bottom: 0;
    width: 100%; height: 44px;
    background: var(--gold);
  }
  .snail {
    position: absolute;
    width: 90px;
    height: 60px;
    top: 196px;
    border-radius: 40px 40px 6px 6px;
  }
  .front__snail { left: 40px; background: var(--gold); }
  .motto {
    position: absolute;
    left: 164px; top: 230px;
    font-size: 17px;
    line-height: 22px;
    font-weight: 700;
    color: var(--gold);
  }

  /* Back */
  .contact {
    position: absolute;
    left: 144px; top: 70px;
    list-style: none;
    color: var(--paper);
    font-size: 15px;
    font-weight: 600;
    line-height: 20px;
  }
  .contact__item { display: flex; align-items: flex-start; margin-bottom: 14px; }
  .contact__icon { width: 20px; height: 20px; margin-right: 10px; flex: none; fill: var(--paper); }
  .back__strip {
    position: absolute;
    left: 0; bottom: 0;
    width: 100%; height: 44px;
    background: var(--paper);
  }
  .back__snail { right: 44px; background: var(--paper); }
</style>
</head>
<body>
  <section class="card card--front">
    <div class="brand">
      <div class="brand__name">
        <span class="brand__the">THE</span>
        <span class="brand__main">CORVELLA</span>
        <span class="brand__spa">SPA</span>
      </div>
      <p class="brand__tagline">a boutique spa for Men &amp; Women</p>
    </div>
    <div class="front__band"></div>
    <div class="snail front__snail" role="img" aria-label="Gold snail illustration"></div>
    <p class="motto">Slow down. Enjoy Life.</p>
  </section>

  <section class="card card--back">
    <ul class="contact">
      <li class="contact__item">
        <svg class="contact__icon" viewBox="0 0 20 20" aria-hidden="true"><path d="M10 2 1 10h3v8h5v-5h2v5h5v-8h3z"/></svg>
        <span>3817 Birch Lane Ashbrook<br>New York 1387</span>
      </li>
      <li class="contact__item">
        <svg class="contact__icon" viewBox="0 0 20 20" aria-hidden="true"><path d="M4 2l3 0 2 5-2 1.5c1 2.2 2.8 4 5 5L13.5 11l5 2v3c0 1.2-1 2-2 2C9 18 2 11 2 4c0-1 .8-2 2-2z"/></svg>
        <span>(607) 462 3085</span>
      </li>
      <li class="contact__item">
        <svg class="contact__icon" viewBox="0 0 20 20" aria-hidden="true"><path d="M1 4h18v1.5l-9 6-9-6z"/><path d="M1 7.5l9 6 9-6V16H1z"/></svg>
        <span>info@thecorvella spa.com</span>
      </li>
    </ul>
    <div class="back__strip"></div>
    <div class="snail back__snail" role="img" aria-label="White snail illustration"></div>
  </section>
</body>
</html>
```